business card design and letterhead for a building inspection company. We have a pre-purchase building and pest inspection ( i inspect house before people purchase it)
Updates

Tilda has been so so responsive and good, i highly recommend her

Industry/Entity Type

Building

Contact Information for Business Card

audience, solicitor, real estate agent, mortgage brokerthe rest of the info will be in the attachement business card

```html
<!DOCTYPE html>
<html lang="en">
<head>
<meta charset="utf-8">
<title>Clearview Property Inspections – Business Card</title>
<link href="https://fonts.googleapis.com/css2?family=Open+Sans:wght@400;600;700&display=swap" rel="stylesheet">
<style>
  :root {
    --backdrop: #e4e4e4;
    --card: #000000;
    --brand-blue: #1674bd;
    --text-light: #ffffff;
  }
  * { margin: 0; padding: 0; box-sizing: border-box; }
  html, body {
    width: 1200px;
    height: 960px;
    overflow: hidden;
    background: var(--backdrop);
    font-family: "Open Sans", sans-serif;
  }
  .canvas { position: relative; width: 1200px; height: 960px; }
  .card {
    position: absolute;
    left: 246px;
    width: 648px;
    height: 380px;
    background: var(--card);
    color: var(--text-light);
  }
  .card--front { top: 66px; }
  .card--back { top: 505px; }

  .brand { position: absolute; display: flex; align-items: center; }
  .brand__mark {
    background: var(--brand-blue);
    border-radius: 50%;
    flex: none;
  }
  .brand__text { display: flex; flex-direction: column; }
  .brand__name {
    color: var(--brand-blue);
    font-weight: 700;
    letter-spacing: 0.02em;
    line-height: 1.05;
  }
  .brand__tagline {
    color: var(--text-light);
    font-weight: 400;
    letter-spacing: 0.06em;
  }

  .card--front .brand { left: 128px; top: 108px; gap: 18px; }
  .card--front .brand__mark { width: 80px; height: 80px; }
  .card--front .brand__name { font-size: 33px; }
  .card--front .brand__tagline { font-size: 13px; margin-top: 6px; }

  .card--back .brand { left: 52px; top: 50px; gap: 14px; }
  .card--back .brand__mark { width: 62px; height: 62px; }
  .card--back .brand__name { font-size: 25px; }
  .card--back .brand__tagline { font-size: 10.5px; margin-top: 5px; }

  .web-band {
    position: absolute;
    left: 0; right: 0;
    top: 278px;
    height: 35px;
    background: var(--brand-blue);
    display: flex;
    align-items: center;
    justify-content: center;
    font-size: 15px;
    letter-spacing: 0.03em;
  }

  .contact-rule {
    position: absolute;
    left: 66px;
    top: 208px;
    width: 360px;
    height: 2px;
    background: var(--brand-blue);
  }
  .person-name {
    position: absolute;
    right: 54px;
    top: 193px;
    font-size: 21px;
    letter-spacing: 0.06em;
    font-weight: 400;
  }
  .person-name strong { font-weight: 700; }
  .contact-list {
    position: absolute;
    right: 54px;
    top: 258px;
    list-style: none;
    text-align: right;
    font-size: 15px;
    line-height: 20.5px;
    letter-spacing: 0.02em;
  }
</style>
</head>
<body>
<main class="canvas">
  <section class="card card--front">
    <div class="brand">
      <span class="brand__mark"></span>
      <div class="brand__text">
        <span class="brand__name">CLEARVIEW PROPERTY INSPECTIONS</span>
        <span class="brand__tagline">The building and pest expert</span>
      </div>
    </div>
    <div class="web-band">www.clearviewinspections.com.au</div>
  </section>

  <section class="card card--back">
    <div class="brand">
      <span class="brand__mark"></span>
      <div class="brand__text">
        <span class="brand__name">CLEARVIEW PROPERTY INSPECTIONS</span>
        <span class="brand__tagline">The building and pest expert</span>
      </div>
    </div>
    <span class="contact-rule"></span>
    <p class="person-name">Sarah <strong>Tilda</strong></p>
    <ul class="contact-list">
      <li>(02) 5550 1284</li>
      <li>0400 555 018</li>
      <li>info@clearviewinspections.com.au</li>
    </ul>
  </section>
</main>
</body>
</html>
```